依頼詳細
販売店舗数45店にて店で配るチラシにも使用。
基本的に店舗にてド注文を頂きますので、フライヤーの下記に注文書などが付いていると
とても便利です。(お客様控え・店舗控え)

大きさはB4サイズ、商品は2品のみです。
商品:おせち料理3段重 13,950円  おせち料理与段重19,500円

三段重と与段(ヨダン)重は縁起を担いでのネーミングです。
詳しくは当社ホームページにて
http://www.kuremadeli.co.jp

記載項目
株式会社クレマデリカ(茨城県 水戸市)
おせち料理監修 株式会社波音鮨東雲グループ(広島県 福山市)

おせち料理三段重 13,950円
おせち料理与段重 19,500円

鮮度とおいしさを追及すると生おせちです。
大きなロブスターとタラバガニを溢れんばかりに詰め込みました。
寿し屋が取り扱う海産物同様、「鮮度は味」をおせち料理で形にしました。

全国配送無料
配送不可能エリア:北海道・沖縄・離島
生おせちなので製造が12月30日にすべての商品を製造します。製造できた商品から冷蔵車
にて発送されるため、関東から北海道内は12月31日に到着しない恐れがあります(天候・道路状況)
そのため、北海道はエリア外とさせて頂きます。

西日本は広島県福山市にて製造・配送を行います。沖縄・離島は上記同様です。

サイズ
B4
ページ数
片面
希望イメージ
シンプル 複雑
単色 カラフル
暗い 明るい
日常 高級
遊び心 厳粛
未来的 伝統的
女性的 男性的
希望する色
全体的に雅な色使い
納品ファイル
• 高解像度JPG (.jpg)
• イラストレーター形式 (.ai)
• フォトショップ形式 (.psd)
補足説明
制作にあたり当社にて今年の商材を撮影をしましたデータを追記致します。
まだ、何ショットかありますが、とりあえず4点追記します。

商品は3段のものと、タラバガニが入った4段(1~3段は同等品)
の2種類です。

宜しくお願いします。
当社おせち料理の成分表を掲載します。
参考までにご利用ください。
おせち料理3段データを追記します。

大変失礼しました。
素材が少ないかもしれませんので、追記します。
ご使用いただければ幸いです。
ご提案の点数が少なく絞り込む材料がないので期間を延長させて頂きます。
いよいよおせち商戦が始まりました。
すでにオーダーが入ってきたために、至急店舗に掲示を致します。
数多くのご参加が頂ければ幸いです。
納得いく作品がまだ出ていないので延長をさせて頂きます。
宜しくお願いします。

商品の写真がさほどいいものではなかったにも関わらず、最大限に魅力を出していただけました。
お客様が商品を選ぶ時に「見易さ・選択肢しやすい」がきちんと作品に出していただけました。

商品の写真が少なかったにも関わらず、たくさんのご参加を頂きましてありがとうございました。会社として大きな商談になる年末の商品は私たちにとってとても大切なものです。
会社社員と店舗の従業員で売りやすさと訴求力を重視して決めさせていただきました。
参加を頂いた皆様に社員一同より御礼申し上げます。

```html
<!DOCTYPE html>
<html lang="ja">
<head>
<meta charset="utf-8">
<title>おせち料理 ご予約チラシ</title>
<link rel="stylesheet" href="https://fonts.googleapis.com/css2?family=Noto+Serif+JP:wght@400;700;900&family=Noto+Sans+JP:wght@400;700&family=Yuji+Mai&display=swap">
<style>
:root{
  --ink:#0d0b0a;
  --red:#c8161d;
  --deep-red:#9e0f14;
  --gold:#c9a24a;
  --gold-light:#ecd28f;
  --white:#ffffff;
  --paper:#ffffff;
  --line:#7a6a5a;
  --text:#222222;
}
*{margin:0;padding:0;box-sizing:border-box}
html,body{width:846px;height:1200px;overflow:hidden;background:var(--paper)}
body{position:relative;font-family:"Noto Serif JP",serif;color:var(--text)}

.hero{position:absolute;left:0;top:0;width:846px;height:892px;background:var(--ink);overflow:hidden}
.hero-photo{position:absolute;left:150px;top:0;width:696px;height:880px;
  background:radial-gradient(ellipse at 70% 60%,#b5382a 0%,#6e1d16 35%,#2a130e 70%,#0d0b0a 100%)}
.tier-photo{position:absolute;left:8px;top:14px;width:140px;height:150px;
  background:linear-gradient(160deg,#5a2a1a,#a8522f 50%,#2b1510)}

.intro{position:absolute;left:168px;top:18px;width:180px;color:var(--white);font-size:11px;line-height:1.7;writing-mode:vertical-rl;height:140px}

.menu{position:absolute;left:8px;top:180px;width:140px;color:var(--white);font-family:"Noto Sans JP",sans-serif;font-size:8.5px;line-height:1.55}
.menu-tier{margin-bottom:12px}
.menu-label{display:inline-block;background:var(--red);color:var(--white);font-family:"Noto Serif JP",serif;font-weight:700;font-size:10px;padding:1px 6px;margin-bottom:4px}

.catch{position:absolute;left:395px;top:175px;height:230px;writing-mode:vertical-rl;color:var(--white);font-size:22px;font-weight:700;line-height:1.6;letter-spacing:.12em;text-shadow:0 0 6px rgba(0,0,0,.8)}
.title{position:absolute;left:318px;top:390px;writing-mode:vertical-rl;font-family:"Yuji Mai",serif;font-size:124px;line-height:1;color:var(--red);text-shadow:0 0 8px rgba(255,255,255,.5)}

.reserve{position:absolute;left:706px;top:14px;width:126px;height:126px;border-radius:50%;background:var(--red);border:3px solid var(--gold-light);color:var(--white);display:flex;align-items:center;justify-content:center;text-align:center;font-weight:900;font-size:22px;line-height:1.25}

.offer{position:absolute;top:722px;display:flex;align-items:center}
.offer-three{left:336px}
.offer-four{left:600px}
.badge{width:80px;height:80px;border-radius:50%;background:radial-gradient(circle,var(--gold-light),var(--gold));display:flex;flex-direction:column;align-items:center;justify-content:center;color:var(--deep-red);font-weight:900;line-height:1.1}
.badge small{font-size:10px}
.badge b{font-size:20px}
.price-block{margin-left:8px;color:var(--white)}
.price-note{font-size:10px;line-height:1.3}
.price{font-weight:900;font-size:34px;color:var(--red);text-shadow:0 0 4px #fff;line-height:1.1}
.price span{font-size:18px}

.band{position:absolute;left:0;top:894px;width:846px;height:36px;background:var(--red);color:var(--white);display:flex;align-items:center;padding-left:10px;font-size:15px;font-weight:700}
.band-tag{background:var(--white);color:var(--red);padding:2px 8px;margin-right:14px;font-size:13px}

.form{position:absolute;top:940px;width:338px;height:250px;border:1px solid var(--line);font-family:"Noto Sans JP",sans-serif;font-size:10px}
.form-customer{left:8px}
.form-store{left:354px}
.form-head{background:#f1e9de;padding:4px 6px;font-weight:700;font-size:11.5px;border-bottom:1px solid var(--line);display:flex;justify-content:space-between}
.form table{width:100%;border-collapse:collapse}
.form th{width:72px;text-align:left;font-weight:400;background:#faf6f0;padding:0 5px;border-bottom:1px solid var(--line);border-right:1px solid var(--line);height:26.3px}
.form td{border-bottom:1px solid var(--line);padding:0 5px;text-align:right}
.form tr:last-child th,.form tr:last-child td{border-bottom:0}

.info{position:absolute;left:702px;top:940px;width:138px;font-family:"Noto Sans JP",sans-serif}
.info h2{color:var(--red);font-family:"Noto Serif JP",serif;font-size:17px;font-weight:900;text-align:center;border-bottom:2px solid var(--red);padding-bottom:3px;margin-bottom:5px}
.info p{font-size:7.5px;line-height:1.55;margin-bottom:6px}
.company{font-family:"Noto Serif JP",serif;font-weight:700;font-size:12px}
.url{font-size:10px;font-weight:700}
</style>
</head>
<body>
<section class="hero">
  <div class="hero-photo" role="img" aria-label="ロブスターとタラバガニを詰めた豪華なおせち重箱の写真"></div>
  <div class="tier-photo" role="img" aria-label="積み重ねたおせち三段重の写真"></div>

  <p class="intro">鮮度とおいしさを追及すると生おせちです。大きなロブスターとタラバガニを溢れんばかりに詰め込みました。寿し屋が取り扱う海産物同様、「鮮度は味」をおせち料理で形にしました。</p>

  <div class="menu">
    <div class="menu-tier"><span class="menu-label">一の重</span><br>数の子・田作り・黒豆<br>伊達巻・栗きんとん<br>紅白かまぼこ・昆布巻<br>錦玉子・海老艶煮</div>
    <div class="menu-tier"><span class="menu-label">二の重</span><br>ロブスター半身・帆立<br>いくら醤油漬・鮭西京焼<br>鰤照焼・たこ桜煮<br>紅白なます・酢蓮根</div>
    <div class="menu-tier"><span class="menu-label">三の重</span><br>筑前煮・椎茸旨煮<br>里芋含め煮・手綱蒟蒻<br>牛八幡巻・鶏松風<br>合鴨ロース・梅人参</div>
    <div class="menu-tier"><span class="menu-label">与の重</span><br>タラバガニ脚・蟹爪<br>ずわい蟹ほぐし身<br>甘海老・焼き帆立</div>
  </div>

  <p class="catch">豪華な詰め合わせで<br>新年を華やかに<br>お迎えください</p>
  <h1 class="title">おせち</h1>

  <div class="reserve">ご予約<br>承り中</div>

  <div class="offer offer-three">
    <div class="badge"><small>全3段</small><b>三段重</b></div>
    <div class="price-block">
      <p class="price-note">厳選素材を丁寧に<br>おせち料理 三段重</p>
      <p class="price">13,950<span>円</span></p>
    </div>
  </div>
  <div class="offer offer-four">
    <div class="badge"><small>豪華4段</small><b>与段重</b></div>
    <div class="price-block">
      <p class="price-note">タラバガニ入り<br>おせち料理 与段重</p>
      <p class="price">19,500<span>円</span></p>
    </div>
  </div>
</section>

<div class="band"><span class="band-tag">早期予約割引特典</span>11月末までご予約の方には波音鮨のクーポン券1,000円分プレゼント!!</div>

<section class="form form-customer">
  <div class="form-head"><span>おせち料理ご予約申込書</span><span>お客様控え</span></div>
  <table>
    <tr><th>ご予約日</th><td>月　　日</td></tr>
    <tr><th>お名前</th><td></td></tr>
    <tr><th>ご住所</th><td></td></tr>
    <tr><th>電話番号</th><td></td></tr>
    <tr><th>三段重</th><td>個</td></tr>
    <tr><th>与段重</th><td>個</td></tr>
    <tr><th>お届け日</th><td>月　　日</td></tr>
    <tr><th>受付店舗</th><td></td></tr>
  </table>
</section>

<section class="form form-store">
  <div class="form-head"><span>おせち料理ご予約申込書</span><span>店舗控え</span></div>
  <table>
    <tr><th>ご予約日</th><td>月　　日</td></tr>
    <tr><th>お名前</th><td></td></tr>
    <tr><th>ご住所</th><td></td></tr>
    <tr><th>電話番号</th><td></td></tr>
    <tr><th>三段重</th><td>個</td></tr>
    <tr><th>与段重</th><td>個</td></tr>
    <tr><th>お届け日</th><td>月　　日</td></tr>
    <tr><th>受付担当</th><td></td></tr>
  </table>
</section>

<aside class="info">
  <h2>全国配送無料</h2>
  <p>配送不可能エリア:北海道・沖縄・離島。生おせちのため12月30日にすべての商品を製造し、冷蔵車にて発送いたします。天候・道路状況により12月31日に到着しない恐れがあるため、北海道はエリア外とさせて頂きます。西日本は広島県福山市にて製造・配送を行います。</p>
  <p>おせち料理監修<br>株式会社波音鮨東雲グループ(広島県 福山市)</p>
  <p class="company">株式会社クレマデリカ<br><small>(茨城県 水戸市)</small></p>
  <p class="url">http://www.kuremadeli.co.jp</p>
</aside>
</body>
</html>
```